Accommodation business card design

We need a business card designed for our long-term accommodation business based in Australia. The business card must match the style of the attached letterhead and logo. The same contact details that are on the letterhead will also go on the card except that the card must list the contact details in the following order:phone, email, home address, ABN.

The card will be printed on .76mm white pvc plastic (same as credit cards), printed both sides and will be silver foil stamped on at least one side (preferably 2 sides) The design template is attached, but please go to www.zt.com.au for more specs.

The only other addition the card will be my name: Malcolm Darby

```html
<!DOCTYPE html>
<html lang="en">
<head>
<meta charset="utf-8">
<title>Highpeak Accommodation – Business Card</title>
<link rel="stylesheet" href="https://fonts.googleapis.com/css2?family=Carlito:wght@400;700&family=Quicksand:wght@400&display=swap">
<style>
  :root {
    --brown: #8a4b40;
    --maroon: #6e1c3c;
    --blush: #ebe1de;
    --white: #ffffff;
    --edge: #6d6d6d;
  }
  html, body {
    margin: 0;
    width: 1200px;
    height: 998px;
    overflow: hidden;
    background: var(--white);
  }
  .canvas { position: relative; width: 1200px; height: 998px; }
  .card {
    position: absolute;
    top: 336px;
    width: 491px;
    height: 307px;
    border: 1px solid var(--edge);
    border-radius: 24px;
    overflow: hidden;
    background: var(--white);
    font-family: "Carlito", "Calibri", sans-serif;
  }
  .card-front { left: 56px; }
  .card-back { left: 659px; background: var(--blush); }
  .card-art { position: absolute; inset: 0; width: 100%; height: 100%; }

  .brand-mark {
    position: absolute;
    left: 85px; top: 43px;
    width: 96px; height: 100px;
    border-radius: 12px;
    background: var(--maroon);
  }
  .brand-name {
    position: absolute;
    left: 197px; top: 46px;
    margin: 0;
    color: var(--brown);
    font-weight: 700;
    line-height: 1;
  }
  .brand-name .line-1 { display: block; font-size: 58px; letter-spacing: 1px; }
  .brand-name .line-2 { display: block; font-size: 27px; letter-spacing: 0.5px; margin-top: 2px; }

  .holder-name {
    position: absolute;
    left: 0; right: 0; top: 36px;
    margin: 0;
    text-align: center;
    font-family: "Quicksand", sans-serif;
    font-weight: 400;
    font-size: 28px;
    color: var(--maroon);
  }
  .contact {
    position: absolute;
    margin: 0;
    font-size: 18.5px;
    color: var(--brown);
    display: flex;
    align-items: center;
    white-space: nowrap;
  }
  .icon {
    width: 20px; height: 20px;
    border-radius: 50%;
    background: var(--white);
    display: inline-flex;
    align-items: center;
    justify-content: center;
    margin-right: 11px;
  }
  .icon svg { width: 12px; height: 12px; fill: var(--brown); }
  .contact-phone { left: 52px; top: 94px; }
  .contact-email { left: 208px; top: 94px; }
  .contact-post { left: 52px; top: 119px; }
  .contact-abn { left: 0; right: 0; top: 148px; justify-content: center; }
</style>
</head>
<body>
<main class="canvas">
  <section class="card card-front" aria-label="Card front">
    <svg class="card-art" viewBox="0 0 491 307" aria-hidden="true">
      <path d="M0 155 Q250 225 491 202 L491 307 L0 307 Z" fill="var(--brown)"/>
      <path d="M118 178 Q330 208 491 146 L491 190 Q300 218 118 178 Z" fill="var(--maroon)"/>
    </svg>
    <div class="brand-mark" aria-hidden="true"></div>
    <h1 class="brand-name"><span class="line-1">HIGHPEAK</span><span class="line-2">ACCOMMODATION</span></h1>
  </section>

  <section class="card card-back" aria-label="Card back">
    <svg class="card-art" viewBox="0 0 491 307" aria-hidden="true">
      <path d="M0 167 C150 215 380 232 491 155 L491 307 L0 307 Z" fill="var(--white)"/>
      <path d="M120 188 Q320 232 491 202 L491 212 Q300 244 120 188 Z" fill="var(--blush)"/>
    </svg>
    <h2 class="holder-name">Malcolm Darby</h2>
    <p class="contact contact-phone">
      <span class="icon"><svg viewBox="0 0 24 24"><path d="M6.6 10.8a15 15 0 0 0 6.6 6.6l2.2-2.2a1 1 0 0 1 1-.25 11.4 11.4 0 0 0 3.6.57 1 1 0 0 1 1 1V20a1 1 0 0 1-1 1A17 17 0 0 1 3 4a1 1 0 0 1 1-1h3.5a1 1 0 0 1 1 1c0 1.25.2 2.45.57 3.57a1 1 0 0 1-.25 1z"/></svg></span>0412 555 308
    </p>
    <p class="contact contact-email">
      <span class="icon"><svg viewBox="0 0 24 24"><path d="M2 5h20v14H2z M2 5l10 8 10-8" /></svg></span>malcolm.darby@mailbox.com
    </p>
    <p class="contact contact-post">
      <span class="icon"><svg viewBox="0 0 24 24"><path d="M12 3 2 12h3v8h5v-5h4v5h5v-8h3z"/></svg></span>PO Box 1183, Harbour Mail Centre QLD 4800
    </p>
    <p class="contact contact-abn">ABN 12 345 678 901</p>
  </section>
</main>
</body>
</html>
```